Rack Card for Portuguese Walking Food Tour

I would like a vertical rack card measuring 99x210mm. Here is the information I would like to include. It does not need to be in this format. We are located in Setubal, Portugal.
Please use the attached Blue Kite Emblem.
Setúbal: Tradition and Today
Experience the culinary delights of Setúbal, Portugal with a walking food tour around our waterfront village. Discover the Mercado do Salgueiral, voted one of the world’s best markets by Daily Meridian, and indulge in local wines and dishes. Prepare for a calm stroll on flat streets. No hills to climb on this tour.
Duration: 4 hours
www.brisklanepasseios.com
+351 265 847 390

```html
<!DOCTYPE html>
<html lang="en">
<head>
<meta charset="utf-8">
<title>Setúbal Tradition &amp; Today – Rack Card</title>
<link href="https://fonts.googleapis.com/css2?family=Poppins:wght@400;500;600;700;800&display=swap" rel="stylesheet">
<style>
  :root {
    --orange: #f26522;
    --charcoal: #3d3d3f;
    --ink: #333335;
    --white: #ffffff;
    --backdrop: #dcdcdc;
    --photo-warm: #e07a4f;
    --photo-light: #f1c7ae;
  }
  * { box-sizing: border-box; margin: 0; padding: 0; }
  html, body { width: 816px; height: 1200px; overflow: hidden; }
  body {
    background: var(--backdrop);
    font-family: "Poppins", sans-serif;
    position: relative;
  }
  .rack-card {
    position: absolute;
    top: 207px;
    width: 370px;
    height: 785px;
    background: var(--white);
    overflow: hidden;
    box-shadow: 4px 6px 10px rgba(0,0,0,0.25);
  }
  .rack-card--front { left: 26px; }
  .rack-card--back { left: 420px; }
  .card-shapes { position: absolute; inset: 0; width: 370px; height: 785px; }
  .centered { position: absolute; left: 0; width: 100%; text-align: center; }

  .brand {
    top: 44px;
    display: flex; align-items: center; justify-content: center; gap: 8px;
    font-weight: 600; font-size: 19px; color: var(--charcoal);
  }
  .brand__dot { width: 22px; height: 22px; border-radius: 50%; background: var(--orange); }

  .title {
    font-weight: 800; color: var(--ink); letter-spacing: -1px; line-height: 1;
  }
  .subtitle { font-weight: 700; color: var(--orange); line-height: 1; }
  .rack-card--front .title { top: 98px; font-size: 70px; }
  .rack-card--front .subtitle { top: 172px; font-size: 28.5px; }

  .tagline { font-weight: 500; font-size: 15.5px; line-height: 20px; }
  .rack-card--front .tagline { top: 596px; color: var(--white); }

  .duration-line {
    top: 680px; font-weight: 700; font-size: 20px; color: var(--white);
    display: flex; justify-content: center; align-items: center; gap: 10px;
  }
  .duration-line__label { color: var(--white); }
  .duration-line__value { color: var(--ink); }
  .duration-line__rule { width: 1px; height: 24px; background: var(--white); }

  .web-pill {
    position: absolute; top: 721px; left: 46px; width: 281px; height: 35px;
    border-radius: 18px; background: var(--charcoal); color: var(--white);
    font-size: 15px; letter-spacing: 1.2px; font-weight: 400;
    display: flex; align-items: center; justify-content: center;
  }
  .web-pill b { font-weight: 600; }

  .rack-card--back .title { top: 28px; font-size: 70px; }
  .rack-card--back .subtitle { top: 100px; font-size: 28.5px; }
  .rack-card--back .tagline { top: 138px; color: var(--ink); }

  .duration-heading { top: 200px; font-weight: 700; font-size: 23px; color: var(--ink); }
  .duration-pill {
    position: absolute; top: 236px; left: 104px; width: 159px; height: 41px;
    border-radius: 21px; background: var(--orange); color: var(--white);
    font-weight: 700; font-size: 24px;
    display: flex; align-items: center; justify-content: center;
  }
  .includes-heading { top: 310px; font-weight: 700; font-size: 31px; color: var(--orange); }

  .includes-list {
    position: absolute; top: 364px; left: 42px; right: 20px;
    list-style: none; color: var(--white); font-size: 16px; line-height: 20px;
  }
  .includes-list li { position: relative; padding-left: 16px; margin-bottom: 20px; }
  .includes-list li svg { position: absolute; left: 0; top: 4px; width: 12px; height: 12px; }

  .call-heading { top: 638px; font-weight: 700; font-size: 26px; color: var(--ink); }
  .phone-line {
    top: 668px; font-weight: 700; font-size: 30px; color: var(--white);
    display: flex; justify-content: center; align-items: center; gap: 10px;
  }
  .phone-line svg { width: 22px; height: 22px; }
</style>
</head>
<body>

<section class="rack-card rack-card--front">
  <svg class="card-shapes" viewBox="0 0 370 785" aria-hidden="true">
    <defs>
      <radialGradient id="catchGradient" cx="50%" cy="45%" r="60%">
        <stop offset="0%" stop-color="#f1c7ae"/>
        <stop offset="60%" stop-color="#e07a4f"/>
        <stop offset="100%" stop-color="#b8583a"/>
      </radialGradient>
    </defs>
    <path d="M0 336 Q185 270 370 336 L370 785 L0 785 Z" fill="var(--charcoal)"/>
    <path d="M0 699 Q185 605 370 699 L370 785 L0 785 Z" fill="var(--orange)"/>
    <circle cx="188" cy="354" r="138" fill="var(--orange)"/>
    <path d="M78 437 L188 583 L298 437 Z" fill="var(--orange)"/>
    <circle cx="188" cy="354" r="125" fill="url(#catchGradient)" role="img" aria-label="Photo of fresh red mullet at the fish market"/>
  </svg>

  <div class="brand centered"><span class="brand__dot"></span>Brisk Lane Passeios</div>
  <h1 class="title centered">SETÚBAL</h1>
  <p class="subtitle centered">TRADITION &amp; TODAY</p>
  <p class="tagline centered">Experience the culinary delights of<br>Setúbal, Portugal</p>
  <div class="duration-line centered">
    <span class="duration-line__label">DURATION</span>
    <span class="duration-line__rule"></span>
    <span class="duration-line__value">4 HOURS</span>
  </div>
  <div class="web-pill">www.<b>brisklanepasseios</b>.com</div>
</section>

<section class="rack-card rack-card--back">
  <svg class="card-shapes" viewBox="0 0 370 785" aria-hidden="true">
    <path d="M0 296 Q185 216 370 296 L370 785 L0 785 Z" fill="var(--charcoal)"/>
    <circle cx="11" cy="227" r="58" fill="var(--orange)"/>
    <path d="M0 663 Q185 577 370 663 L370 785 L0 785 Z" fill="var(--orange)"/>
  </svg>

  <h2 class="title centered">SETÚBAL</h2>
  <p class="subtitle centered">TRADITION &amp; TODAY</p>
  <p class="tagline centered">Experience the culinary delights of<br>Setúbal, Portugal</p>
  <p class="duration-heading centered">DURATION</p>
  <div class="duration-pill">4 HOURS</div>
  <p class="includes-heading centered">THIS INCLUDES</p>

  <ul class="includes-list">
    <li><svg viewBox="0 0 12 12"><rect x="0.75" y="1.75" width="9.5" height="9.5" rx="1" fill="none" stroke="var(--orange)" stroke-width="1.5"/><path d="M3 6.5 L5.2 8.6 L11.2 1.5" fill="none" stroke="var(--orange)" stroke-width="1.8"/></svg>A walking food tour around our waterfront village.</li>
    <li><svg viewBox="0 0 12 12"><rect x="0.75" y="1.75" width="9.5" height="9.5" rx="1" fill="none" stroke="var(--orange)" stroke-width="1.5"/><path d="M3 6.5 L5.2 8.6 L11.2 1.5" fill="none" stroke="var(--orange)" stroke-width="1.8"/></svg>Discover the Mercado do Salgueiral, voted one of the world’s best markets by Daily Meridian</li>
    <li><svg viewBox="0 0 12 12"><rect x="0.75" y="1.75" width="9.5" height="9.5" rx="1" fill="none" stroke="var(--orange)" stroke-width="1.5"/><path d="M3 6.5 L5.2 8.6 L11.2 1.5" fill="none" stroke="var(--orange)" stroke-width="1.8"/></svg>Indulge in local wines and dishes.</li>
    <li><svg viewBox="0 0 12 12"><rect x="0.75" y="1.75" width="9.5" height="9.5" rx="1" fill="none" stroke="var(--orange)" stroke-width="1.5"/><path d="M3 6.5 L5.2 8.6 L11.2 1.5" fill="none" stroke="var(--orange)" stroke-width="1.8"/></svg>Prepare for a calm stroll on flat streets.</li>
  </ul>

  <p class="call-heading centered">Call Us</p>
  <div class="phone-line centered">
    <svg viewBox="0 0 24 24" aria-hidden="true"><path d="M6.6 10.8a15.2 15.2 0 0 0 6.6 6.6l2.2-2.2a1 1 0 0 1 1-.25 11.4 11.4 0 0 0 3.6.57 1 1 0 0 1 1 1V20a1 1 0 0 1-1 1A17 17 0 0 1 3 4a1 1 0 0 1 1-1h3.5a1 1 0 0 1 1 1c0 1.25.2 2.45.57 3.57a1 1 0 0 1-.25 1z" fill="var(--ink)"/></svg>
    +351 265 847 390
  </div>
  <div class="web-pill">www.<b>brisklanepasseios</b>.com</div>
</section>

</body>
</html>
```